Design the Marketing Brochure for a service company with Vantage 500 Clients

We need to redesign our marketing brochures to reflect the new service lines we have added in the last few years. We are a professional staffing firm based in Miami, Florida and have a portfolio of clients that include: Coral Meridian, Bluewave Voyage Lines, Patty Palace Corp, Horizon Lens Network Etc. I have attached our current marketing inserts in pdf format. I would like to have 5 inserts displaying our services, process and business lines.

Target Market(s)

Vantage 1000 companies. Within those companies our clients are: CFO's, VP of Finance, Controller, Head of Human Resources, Banking Executives etc. All financial related roles.

Industry/Entity Type

Recruitment

Colors
ec1f27
ffffff
aaaaaa
fece3e
000000

Requirements
Must have
• 5 pages 3 of which we have mots of the content. One page dedicated to " Temporary Staffing" and one page dedicated to our "Banking Division" The brochures should include professional pictures and a well designed layout that looks professional and appealing to an educated client. Our colors are Red, Gray and White.
• Please see our attached brochures and our website at www.kvotalent.example
Nice to have
• Professional pictures of people in the business workplace.
Should not have
• Graphics or cartoons of any kind.

```html
<!DOCTYPE html>
<html lang="en">
<head>
<meta charset="utf-8">
<title>Kavo Talent Partners – Service Inserts</title>
<link href="https://fonts.googleapis.com/css2?family=Cinzel:wght@400;600&family=Lato:wght@400;700&display=swap" rel="stylesheet">
<style>
:root{
  --red:#c01a22;
  --red-bright:#ec1f27;
  --gray:#aaaaaa;
  --gray-dark:#4a4a4a;
  --gold:#d9a930;
  --ink:#2b2b2b;
  --stage:#e6e6e6;
  --white:#ffffff;
}
*{box-sizing:border-box;margin:0;padding:0}
html,body{width:1200px;height:1200px;overflow:hidden}
body{background:var(--stage);font-family:'Lato',sans-serif;color:var(--ink);position:relative}
.page{position:absolute;width:340px;height:440px;background:var(--white);overflow:hidden;box-shadow:0 4px 14px rgba(0,0,0,.25)}
.page--overview{left:45px;top:122px}
.page--process{left:435px;top:122px}
.page--expertise{left:825px;top:115px}
.page--temp{left:255px;top:660px}
.page--banking{left:668px;top:660px}

.hero{position:absolute;left:0;top:0;width:100%;height:160px;background:linear-gradient(160deg,#ededed,#c9c9c9);clip-path:polygon(0 0,100% 0,100% 88%,0 70%)}
.band{position:absolute;height:22px;background:var(--red);clip-path:polygon(0 0,100% 30%,100% 100%,0 68%)}
.portrait{position:absolute;border-radius:50%;border:3px solid var(--red);box-shadow:0 0 0 3px var(--white),0 2px 6px rgba(0,0,0,.3)}
.photo{position:absolute}

.brand{position:absolute;display:flex;align-items:center;gap:4px}
.brand__dot{width:7px;height:7px;border-radius:50%;background:var(--gray-dark)}
.brand__name{font-family:'Lato',sans-serif;font-weight:700;font-size:8.5px;color:var(--gray-dark);letter-spacing:.2px}

.title{position:absolute;font-family:'Cinzel',serif;font-size:13px;color:var(--gold);letter-spacing:.6px}
.lead{position:absolute;font-size:4.3px;line-height:1.4;color:#444;text-align:justify}
.h{font-size:8px;font-weight:700;color:var(--red);text-transform:uppercase;letter-spacing:.2px}
.h--sm{font-size:6px}
.sub{font-size:4.4px;font-weight:700;color:#222;margin:2px 0}
.p{font-size:4px;line-height:1.4;color:#444;text-align:justify;margin-bottom:4px}
.list{list-style:none;font-size:3.9px;line-height:1.55;color:#444}
.list li::before{content:"•";color:var(--red);margin-right:2px}
.block{position:absolute}

.foot{position:absolute;left:0;bottom:9px;width:262px;height:17px;background:var(--red);color:var(--white);font-size:4px;display:flex;align-items:center;gap:6px;padding-left:9px;white-space:nowrap}
.foot span{display:flex;align-items:center;gap:2px;line-height:1.2}
.foot i{display:inline-block;width:4px;height:4px;border-radius:50%;background:var(--gold)}
.tabs{position:absolute;right:14px;bottom:9px;display:flex;gap:3px}
.tabs b{display:block;width:22px;height:17px;transform:skewX(-20deg)}
.tabs b:first-child{background:var(--gray)}
.tabs b:last-child{background:var(--gray-dark)}

.step{position:relative;height:32px;margin-bottom:5px;padding:5px 0 0 10px;clip-path:polygon(0 0,88% 0,100% 50%,88% 100%,0 100%)}
.step--light{background:#d4d4d4;color:#333}
.step--dark{background:#505050;color:var(--white)}
.step h4{font-size:6.6px;font-weight:400}
.step p{font-size:3.6px;line-height:1.35;opacity:.85}

.cols{position:absolute;display:flex;gap:14px}
.col h5{font-size:5.4px;color:var(--red);font-weight:700;margin-bottom:3px}
</style>
</head>
<body>

<!-- Overview -->
<section class="page page--overview">
  <div class="hero"></div>
  <div class="portrait" style="left:22px;top:18px;width:126px;height:126px;background:radial-gradient(circle at 55% 45%,#6f8fb0,#2c4a6b 70%,#1b2f46)" role="img" aria-label="Businessman touching a glowing world network display"></div>
  <div class="brand" style="left:180px;top:22px"><span class="brand__dot"></span><span class="brand__name">Kavo Talent Partners</span></div>
  <div class="title" style="left:206px;top:44px">Overview</div>
  <p class="lead" style="left:176px;top:64px;width:150px">Kavo Talent Partners is a specialized professional recruitment firm built with a global economy in mind. We provide customized human capital solutions including Executive Recruitment, Direct Hire and Temporary Staffing, to both domestic and international organizations from our headquarters in Miami, Florida. Our functional areas of expertise include: Accounting, Finance and Human Resources.</p>
  <div class="band" style="left:100px;top:126px;width:250px"></div>
  <div class="photo" style="left:190px;top:160px;width:148px;height:250px;background:linear-gradient(180deg,#f4f4f4,#3a3a3a 40%,#222)" role="img" aria-label="Businessman in a dark suit holding a leather portfolio"></div>
  <div class="block" style="left:13px;top:160px;width:170px">
    <div class="h">Candidate Focused</div>
    <p class="p" style="margin-top:3px">An effective job search begins with choosing the right recruiting firm to represent and guide you through the entire job search process. At Kavo Talent Partners, we are not only partners to our clients, but also our candidates. We are Career Consultants not just recruiters. There is a big difference. We believe in fostering long-term relationships with the candidates we represent and advise and guide them toward the right role in the right company.</p>
    <p class="p">Our methodology is simple. We take the time to get to know you, to see what makes you tick, what keeps you up at night and where you'd like to take your career now and into the future.</p>
    <div class="h" style="margin-top:4px">Our Process</div>
    <div class="sub">When you meet with a Search Consultant at Kavo Talent Partners:</div>
    <ul class="list">
      <li>We will schedule an in person meeting</li>
      <li>We listen to your short and long term career goals and create a filter</li>
      <li>We learn about your biggest accomplishments</li>
      <li>We provide job search advice</li>
      <li>We advocate you, not your resume</li>
      <li>We screen the leading teams in the region to find your perfect fit</li>
    </ul>
    <p class="p" style="margin-top:4px">Wherever you fit in this vast Accounting, Finance and HR world, we have you covered. We deliver customized job opportunity searches based on your goals and achievements, not just your resume, and proactively market your amazing talents to our vast client-based network.</p>
    <p class="p">Our Miami and Ft Lauderdale Accounting and Finance job opportunities include Permanent Direct Hire and Contract Project Solutions for a wide range of financial consultants and candidates.</p>
  </div>
  <div class="foot"><span><i></i>(555) 014-2290</span><span><i></i>info@kvotalent.example</span><span><i></i>www.kvotalent.example</span><span><i></i>4410 Harbor Crest Way Suite 210<br>Miami, FL 33100</span></div>
  <div class="tabs"><b></b><b></b></div>
</section>

<!-- Process -->
<section class="page page--process">
  <div class="hero" style="background:linear-gradient(160deg,#d8d8d8,#9d9d9d)" role="img" aria-label="Soft grey image of a business handshake"></div>
  <div class="portrait" style="left:20px;top:48px;width:130px;height:130px;background:radial-gradient(circle at 50% 40%,#c9ced6,#6b7480 65%,#3d444d)" role="img" aria-label="Smiling businessman shaking hands in an office"></div>
  <div class="brand" style="left:196px;top:44px"><span class="brand__dot"></span><span class="brand__name">Kavo Talent Partners</span></div>
  <div class="title" style="left:212px;top:72px">Our Process</div>
  <div class="band" style="left:170px;top:132px;width:180px"></div>
  <div class="block" style="left:0;top:204px;width:160px">
    <div class="step step--light"><h4>Kickoff Activities</h4><p>› Assess organization &amp; position<br>› Develop specification</p></div>
    <div class="step step--dark"><h4>Candidate Identification</h4><p>› Contact sources &amp; potential candidates<br>› Screen candidates<br>› Present initial candidate</p></div>
    <div class="step step--light"><h4>Candidate Qualification</h4><p>› Heavy recruiting continues<br>› Review progress</p></div>
    <div class="step step--dark"><h4>Candidate Selection</h4><p>› Reference reporting<br>› Client final interviews<br>› Offer negotiations &amp; candidate counseling</p></div>
  </div>
  <div class="block" style="left:176px;top:182px;width:150px">
    <div class="h h--sm">Need to hire someone?</div>
    <p style="font-size:5.8px;line-height:1.3;color:#333;margin:2px 0 8px">We can successfully access domestic and Latin American markets to match your organizations needs with ideal candidates.</p>
    <div class="h h--sm" style="font-size:5.4px">Our Approach</div>
    <p class="p">The challenge of finding talent in a global business environment is best met with the support of a firm with a proven track record of success. Kavo Talent Partners utilizes a unique perspective regarding culture, performance, leadership, and organizational fit. This approach ensures that new hires are integrated rapidly and successfully and eliminates setbacks.</p>
    <div class="h h--sm" style="font-size:5.4px">Seamless Recruitment Process</div>
    <ul class="list" style="margin:2px 0 6px">
      <li>Excellent research capabilities and access to a global talent pool</li>
      <li>Extensive assessment methodology</li>
      <li>In depth reference checking</li>
      <li>Critical contribution to the successful completion of the search</li>
    </ul>
    <div class="h h--sm" style="font-size:5.4px">Our goal is to be your business<br>partner not just your vendor</div>
    <p class="p" style="margin-top:2px">At Kavo Talent Partners, partnership is part of our more important core values. We understand the challenge of finding talent in a global business environment and are prepared to support your organization.</p>
    <p class="p">We utilize a unique perspective regarding culture, performance, leadership, and organizational fit. This approach ensures that new hires are integrated rapidly and successfully.</p>
  </div>
  <div class="foot"><span><i></i>(555) 014-2290</span><span><i></i>info@kvotalent.example</span><span><i></i>www.kvotalent.example</span><span><i></i>4410 Harbor Crest Way Suite 210<br>Miami, FL 33100</span></div>
  <div class="tabs"><b></b><b></b></div>
</section>

<!-- Expertise -->
<section class="page page--expertise">
  <div class="hero"></div>
  <div class="portrait" style="left:26px;top:22px;width:130px;height:130px;background:radial-gradient(circle at 50% 45%,#d6d2cc,#8a8580 60%,#4c4845)" role="img" aria-label="Business team reviewing documents at a meeting table"></div>
  <div class="brand" style="left:200px;top:26px"><span class="brand__dot"></span><span class="brand__name">Kavo Talent Partners</span></div>
  <div class="title" style="left:196px;top:48px">Our Expertise</div>
  <p class="lead" style="left:194px;top:70px;width:135px">Our expertise ranges from <b>Executive Recruitment, Direct Hire, Temporary Contractors</b> to Consultants. We are a tactical partner to companies looking to proactively respond to the changes impacting the Accounting, Finance and Human Resources functions.</p>
  <div class="band" style="left:150px;top:128px;width:200px"></div>
  <p class="lead" style="left:22px;top:174px;width:305px">Our clients rely on our unparalleled experience in evaluating and qualifying highly skilled professionals to their current and future openings. We specialize in the following roles:</p>
  <div class="cols" style="left:22px;top:190px">
    <div class="col" style="width:100px"><h5>Accounting</h5><ul class="list"><li>Chief Financial Officer</li><li>Treasurer</li><li>Director of Accounting</li><li>Director of Financial Reporting</li><li>Corporate Controller</li><li>Controller</li><li>Assistant Controller</li><li>Divisional Controller (Latin America)</li><li>Assistant Treasurer</li><li>VP of Tax</li><li>Tax Director (Domestic/International)</li><li>Tax Manager (Domestic/International)</li><li>VP of Internal Audit</li><li>Director of Internal Audit</li><li>Director of Information Systems Audit</li><li>Chief Financial Officer</li><li>Treasurer</li><li>Director of Accounting</li><li>Director of Financial Reporting</li><li>Corporate Controller</li><li>Controller</li><li>Assistant Controller</li><li>Divisional Controller (Latin America)</li><li>Assistant Treasurer</li><li>VP of Tax</li><li>Tax Director (Domestic/International)</li><li>Tax Manager (Domestic/International)</li><li>VP of Internal Audit</li><li>Director of Internal Audit</li><li>Director of Information Systems Audit</li></ul></div>
    <div class="col" style="width:96px"><h5>Finance</h5><ul class="list"><li>VP of Finance</li><li>Director of Finance</li><li>Chief Compliance Officer</li><li>Chief Audit Officer</li><li>Chief Risk Officer</li><li>Compliance Director</li><li>Compliance Officer</li><li>Business Development Officer</li><li>Business Development Manager (Latin America)</li><li>Strategic Planning Manager</li><li>Finance Manager</li><li>Market Risk Manager</li><li>Portfolio Manager</li><li>Managing Director</li><li>Fund Manager</li><li>Credit Manager</li><li>Senior Credit Analyst</li><li>Senior Financial Analyst</li><li>Business Analyst</li><li>Investment Banking Analyst</li></ul></div>
    <div class="col" style="width:80px"><h5>Human Resources</h5><ul class="list"><li>VP of Finance</li><li>Director of Finance</li><li>Chief Compliance Officer</li><li>Chief Audit Officer</li><li>Chief Risk Officer</li><li>Compliance Director</li><li>Compliance Officer</li><li>Business Development Officer</li><li>Business Development Manager (Latin America)</li><li>Strategic Planning Manager</li><li>HRIS Specialist</li><li>Payroll Manager</li><li>Payroll Coordinator</li><li>Payroll Specialist</li><li>Benefits Manager</li><li>Benefits Analyst</li><li>Benefits Coordinator</li><li>Compensation Manager</li><li>Compensation Analyst</li></ul></div>
  </div>
  <div class="photo" style="left:130px;top:345px;width:200px;height:70px;background:linear-gradient(180deg,rgba(255,255,255,0),#6d6a66 45%,#3b3936)" role="img" aria-label="Three young professionals in suits standing together"></div>
  <div class="foot"><span><i></i>(555) 014-2290</span><span><i></i>info@kvotalent.example</span><span><i></i>www.kvotalent.example</span><span><i></i>4410 Harbor Crest Way Suite 210<br>Miami, FL 33100</span></div>
  <div class="tabs"><b></b><b></b></div>
</section>

<!-- Temporary Staffing -->
<section class="page page--temp">
  <div class="hero" style="height:200px;background:linear-gradient(120deg,#f2f2f2,#9e9e9e 55%,#e4e4e4);clip-path:polygon(0 0,100% 0,100% 62%,0 90%)" role="img" aria-label="Hand resting on a computer mouse in black and white"></div>
  <div class="brand" style="left:190px;top:28px"><span class="brand__dot"></span><span class="brand__name">Kavo Talent Partners</span></div>
  <div class="band" style="left:0;top:156px;width:160px;transform:scaleY(-1)"></div>
  <div class="portrait" style="left:190px;top:72px;width:130px;height:130px;background:radial-gradient(circle at 50% 45%,#e0d4c4,#9a8770 60%,#4e4236)" role="img" aria-label="Two smiling businesswomen working at a desk"></div>
  <div class="title" style="left:100px;top:232px">Temporary Staffing</div>
  <div class="block" style="left:17px;top:275px;width:150px">
    <div class="h h--sm">Flexible Accounting Staffing<br>Solutions</div>
    <p class="p" style="margin-top:3px">You can hire highly skilled professionals from Kavo Talent Partners in three different ways:</p>
    <div class="sub">TEMPORARY:</div>
    <p class="p">Supplement your full-time staff on a project basis. This staffing solution is effective when ongoing productivity and cost management are essential.</p>
    <div class="sub">TEMPORARY-TO-HIRE:</div>
    <p class="p">Quickly staff a vacant position with the option to hire full time. This staffing solution is effective when you want to assess fit before you make a hiring decision.</p>
    <p class="p">Staffing support for long-term projects. This staffing solution is effective for long-term or recurring projects that require a specialized skill set.</p>
  </div>
  <div class="block" style="left:188px;top:300px;width:140px">
    <div class="sub" style="font-size:4.6px">AREAS OF ACCOUNTING STAFFING EXPERTISE:</div>
    <p class="p">Here are just a few of our specialty areas:</p>
    <div style="display:flex;gap:18px">
      <ul class="list"><li>Accounting Clerk</li><li>Accounting Manager</li><li>Accounts Payable</li><li>Accounts Receivable</li><li>Auditor</li><li>Billing</li><li>Bookkeeping</li><li>Cost Accounting</li></ul>
      <ul class="list"><li>Credit &amp; Collections</li><li>Data Entry Clerk</li><li>Financial Analyst</li><li>Financial Services</li><li>Payroll</li><li>Senior Accountant</li><li>Staff Accountant</li><li>Tax Accounting</li></ul>
    </div>
  </div>
  <div class="foot"><span><i></i>(555) 014-2290</span><span><i></i>info@kvotalent.example</span><span><i></i>www.kvotalent.example</span><span><i></i>4410 Harbor Crest Way Suite 210<br>Miami, FL 33100</span></div>
  <div class="tabs"><b></b><b></b></div>
</section>

<!-- Banking Division -->
<section class="page page--banking">
  <div class="hero" style="height:180px;background:linear-gradient(150deg,#8a8a8a,#d9d9d9 45%,#f2f2f2);clip-path:polygon(0 0,100% 0,100% 62%,0 100%)" role="img" aria-label="Close-up of a calculator and financial papers in grey tones"></div>
  <div class="brand" style="left:44px;top:54px"><span class="brand__dot"></span><span class="brand__name">Kavo Talent Partners</span></div>
  <div class="title" style="left:45px;top:75px">Banking Division</div>
  <div class="portrait" style="left:200px;top:50px;width:126px;height:126px;background:radial-gradient(circle at 55% 40%,#f3efe4,#c9b68a 55%,#7e6a45)" role="img" aria-label="Alarm clock beside stacks of coins"></div>
  <div class="band" style="left:0;top:150px;width:180px;transform:scaleY(-1)"></div>
  <div class="block" style="left:0;top:186px;width:340px;text-align:center">
    <div class="h" style="font-size:9px">Finance and</div>
    <div class="h" style="font-size:6.4px">Accounting Staffing Professionals</div>
  </div>
  <div class="block" style="left:14px;top:220px;width:150px">
    <p class="p">When you come to Kavo Talent Partners with a staffing request, we will ask you to provide a job description, a list of skills you desire in a candidate, any qualifications unique to your organization and the length of time you anticipate needing the extra assistance. We will then match you with pre-evaluated finance and accounting professionals with the skills and experience required for your business needs.</p>
    <p class="p">We want your experience with us to exceed your expectations. We will listen to your needs and help you implement the best staffing services for your organization. If you are not satisfied, simply notify us within the first eight hours of the assignment.</p>
    <p class="p">Speak with an accounting recruiter to discuss your temporary staffing needs or learn more about our services and guarantee.</p>
    <div class="sub">When you're adjusting to an influx of new business</div>
    <p class="p">New business is a good thing, right? It may not feel like it if you don't have the staff to take on the extra workload. In fact, new business could mean big headaches if your staff is already stressed or customers notice a drop in quality.</p>
    <p class="p">A good course of action may be to contact temp staffing agencies serving your area for help during the transition. After all, finding highly skilled accounting professionals can be a time-consuming process.</p>
    <p class="p">A good agency will evaluate a candidate's work history and conduct face-to-face interviews, assess software skills and conduct accounting knowledge evaluation tests.</p>
  </div>
  <div class="block" style="left:176px;top:220px;width:150px">
    <div class="sub">When the team is overworked</div>
    <p class="p">Has your staff been missing deadlines or arriving to work late? Before threatening to substitute this year's bonuses with alarm clocks, you need to assess the cause of these issues. It could be because they're overworked. Other warning signs of an unmanageable workload include team members who are suddenly making more mistakes than usual.</p>
    <p class="p">Give your staff some relief by bringing in support from temp staffing agencies. A temporary accounting professional can help you address your workplace's immediate needs. During that time, you'll have an opportunity to observe the temporary staff member's performance firsthand.</p>
    <div class="sub">When top performers lack the know-how</div>
    <p class="p">You know who your top performers are. They're your go-to accounting professionals who would be in the Ledger League All-Star Game every year, if one existed. But sometimes even they can't handle the specialized tasks that arise.</p>
    <p class="p">A specialized temporary accounting professional can come in for the duration of the project and provide the expertise your core team lacks. He or she can even train your team members so they can handle similar situations in the future.</p>
    <p class="p">Temp staffing agencies offer you a way to handle increased business, heavy workloads or specialty projects that may be beyond your team's current capacity.</p>
  </div>
  <div class="foot"><span><i></i>(555) 014-2290</span><span><i></i>info@kvotalent.example</span><span><i></i>www.kvotalent.example</span><span><i></i>4410 Harbor Crest Way Suite 210<br>Miami, FL 33100</span></div>
  <div class="tabs"><b></b><b></b></div>
</section>

</body>
</html>
```